Business Card Design Project

We are rebranding an existing automotive collision repair business. The business is called harrowell works. I have attached logo but I'm not tied to that. I want to leave this wide open.

I want this card to say we are professional, competent, cutting edge. We are focused on customers and use a lot of the latest technology to make the customer experience different. We sign customers in on Vextabs. Paperwork I signed electronically and updates are sent via text, email, logging on a website or as they wish. I want this innovation and image to come through in our cards

Target Market(s)

60%. Women 40% men. Age 35-60

Industry/Entity Type

Automotive

Requirements
Must have
• The card must have name, title, phone,email, cell, web page

```html
<!DOCTYPE html>
<html lang="en">
<head>
<meta charset="utf-8">
<title>harrowell works – business card</title>
<link rel="stylesheet" href="https://fonts.googleapis.com/css2?family=Open+Sans:wght@400;600;700&display=swap">
<style>
  :root {
    --stage: #ececec;
    --card: #f4f4f4;
    --ink: #1c1c1c;
    --green: #77b82a;
    --black: #0d0d0d;
  }
  * { box-sizing: border-box; margin: 0; padding: 0; }
  html, body { width: 1200px; height: 931px; overflow: hidden; }
  body {
    background: var(--stage);
    font-family: "Open Sans", Arial, sans-serif;
    color: var(--ink);
    display: flex;
    align-items: center;
    justify-content: center;
  }
  .business-card {
    position: relative;
    width: 1000px;
    height: 571px;
    background: var(--card);
    overflow: hidden;
    box-shadow: 0 10px 30px rgba(0,0,0,0.12);
  }
  .card-wave {
    position: absolute;
    inset: 0;
    width: 100%;
    height: 100%;
  }
  .contact-block {
    position: absolute;
    left: 110px;
    top: 120px;
  }
  .person-name {
    font-size: 34px;
    font-weight: 700;
    line-height: 1.15;
  }
  .person-title {
    font-size: 32px;
    font-weight: 400;
    line-height: 1.15;
    margin-bottom: 38px;
  }
  .address-row {
    display: flex;
    align-items: flex-start;
    gap: 14px;
    font-size: 19px;
    line-height: 1.3;
    margin-bottom: 26px;
  }
  .contact-list { list-style: none; }
  .contact-list li {
    display: flex;
    align-items: center;
    gap: 14px;
    font-size: 19px;
    line-height: 1.35;
  }
  .icon { width: 20px; height: 20px; flex: none; fill: var(--green); }
  .brand-name {
    position: absolute;
    left: 560px;
    top: 190px;
    white-space: nowrap;
    font-size: 48px;
    font-weight: 700;
    line-height: 1.2;
    color: var(--green);
  }
</style>
</head>
<body>
  <main class="business-card">
    <svg class="card-wave" viewBox="0 0 1000 571" preserveAspectRatio="none" aria-hidden="true">
      <path d="M0 500 C 260 440, 560 470, 760 420 S 950 360, 1000 355 L1000 571 L0 571 Z" fill="var(--black)"/>
      <path d="M0 500 C 260 440, 560 470, 760 420 S 950 360, 1000 355" fill="none" stroke="var(--green)" stroke-width="7"/>
      <path d="M600 450 C 740 370, 870 320, 1000 290" fill="none" stroke="var(--green)" stroke-width="2.5"/>
    </svg>

    <section class="contact-block">
      <h1 class="person-name">Dario Kessling</h1>
      <p class="person-title">Owner</p>

      <div class="address-row">
        <svg class="icon" viewBox="0 0 24 24"><path d="M12 2a7 7 0 0 0-7 7c0 5 7 13 7 13s7-8 7-13a7 7 0 0 0-7-7zm0 9.5A2.5 2.5 0 1 1 12 6.5a2.5 2.5 0 0 1 0 5z"/></svg>
        <p>418 Orchard Pike east Marlow,<br>NJ 07399</p>
      </div>

      <ul class="contact-list">
        <li>
          <svg class="icon" viewBox="0 0 24 24"><path d="M7 1h10a2 2 0 0 1 2 2v18a2 2 0 0 1-2 2H7a2 2 0 0 1-2-2V3a2 2 0 0 1 2-2zm0 3v14h10V4zm5 15.5a1 1 0 1 0 0 2 1 1 0 0 0 0-2z"/></svg>
          <span>555-214-0387</span>
        </li>
        <li>
          <svg class="icon" viewBox="0 0 24 24"><path d="M6.6 10.8a15 15 0 0 0 6.6 6.6l2.2-2.2a1 1 0 0 1 1-.25 11.4 11.4 0 0 0 3.6.57 1 1 0 0 1 1 1V20a1 1 0 0 1-1 1A17 17 0 0 1 3 4a1 1 0 0 1 1-1h3.5a1 1 0 0 1 1 1c0 1.25.2 2.45.57 3.57a1 1 0 0 1-.25 1z"/></svg>
          <span>555-214-0392</span>
        </li>
        <li>
          <svg class="icon" viewBox="0 0 24 24"><path d="M2 5h20v14H2zm2 2v.5l8 5 8-5V7zm0 3v7h16v-7l-8 5z"/></svg>
          <span>dario@harrowellworks.com</span>
        </li>
        <li>
          <svg class="icon" viewBox="0 0 24 24"><path d="M12 2a10 10 0 1 0 0 20 10 10 0 0 0 0-20zm6.9 6h-2.9a15 15 0 0 0-1.4-3.6A8 8 0 0 1 18.9 8zM12 4a13 13 0 0 1 1.9 4h-3.8A13 13 0 0 1 12 4zM4.3 14a8 8 0 0 1 0-4h3.4a16 16 0 0 0 0 4zm.8 2h2.9a15 15 0 0 0 1.4 3.6A8 8 0 0 1 5.1 16zM8 8H5.1a8 8 0 0 1 4.3-3.6A15 15 0 0 0 8 8zm4 12a13 13 0 0 1-1.9-4h3.8A13 13 0 0 1 12 20zm2.3-6H9.7a14 14 0 0 1 0-4h4.6a14 14 0 0 1 0 4zm.3 5.6A15 15 0 0 0 16 16h2.9a8 8 0 0 1-4.3 3.6zM16.3 14a16 16 0 0 0 0-4h3.4a8 8 0 0 1 0 4z"/></svg>
          <span>www.harrowellworks.com</span>
        </li>
      </ul>
    </section>

    <div class="brand-name">harrowell works</div>
  </main>
</body>
</html>
```